Harbour Vale Lettings Web Site Design

I am after a very simple 3 page web site please. I attach a PDF with the text and information. The logo is also in the PDF. The colours should be orange and blues. The pages should be HOME - LANDLORDS - TENANTS.
Lettings and Property Management Company aimed at just being a reference point for tenants but more of a sales pitch to landlords. Please refer to the attached PDF and word file which contains far more content for the various pages.

Target Market(s)

Prospective Landlords mainly but tenants also

Industry/Entity Type

Lettings and Property Management

Number of Pages Required

3 page

Font styles to use
Sans Serif
Other font styles liked:
• Candara

Colors
0054AA
0677BA
7BADD7
CADEEF
E8F1F8
F0912C
F2A743
F7CA91
FBE8D2
FDF5EE

Requirements
Must have
• Must be colour co-ordinated to the logo (orange and dark blue predominently, Must have good quality stock images relating to property and renting out property. Should have home page and links to landlord page and tenant page. Must have the 4 logos that we are affiliated to (TKR, Tenancy Settle, BNF and Funds Guard Scheme) - all attached.
Nice to have
• Modern feel, crisp and sharp but simple - good stock images.

```html
<!DOCTYPE html>
<html lang="en">
<head>
<meta charset="utf-8">
<title>Harbour Vale Lettings – Property Management</title>
<link rel="stylesheet" href="https://fonts.googleapis.com/css2?family=Montserrat:wght@400;500;600;700;800&display=swap">
<style>
  :root {
    --orange: #e8891a;
    --sky-blue: #13a8d3;
    --navy: #1b2d5e;
    --ink: #333333;
    --light-band: #f3f3f3;
    --footer: #262626;
    --white: #ffffff;
    --font: "Montserrat", sans-serif;
  }
  * { box-sizing: border-box; margin: 0; padding: 0; }
  html, body { width: 720px; height: 1200px; overflow: hidden; }
  body { position: relative; font-family: var(--font); color: var(--ink); background: var(--white); }

  .hero { position: absolute; left: 0; top: 0; width: 720px; height: 432px; overflow: hidden; }
  .hero-photo {
    position: absolute; inset: 0;
    background:
      linear-gradient(180deg, #6f8ea6 0%, #8aa3b6 18%, #5f7f98 30%, #3d6688 42%, #2f5a7c 58%, #4d6650 72%, #5e6a3e 85%, #3f4a2c 100%);
  }
  .hero-photo::after {
    content: ""; position: absolute; inset: 0;
    background: linear-gradient(90deg, rgba(0,0,0,0.05) 0%, rgba(0,0,0,0) 50%, rgba(60,70,30,0.35) 100%);
  }
  .hero-cut { position: absolute; left: 0; bottom: 0; width: 720px; height: 58px; }

  .brand { position: absolute; display: flex; align-items: center; gap: 6px; }
  .brand-dot { width: 14px; height: 14px; border-radius: 50%; background: var(--orange); flex: none; }
  .brand-name { font-size: 10px; font-weight: 600; letter-spacing: 0.5px; color: var(--white); line-height: 1.2; }
  .header-brand { left: 45px; top: 42px; width: 140px; }

  .main-nav { position: absolute; top: 37px; right: 44px; display: flex; align-items: center; gap: 26px; }
  .main-nav a { font-size: 8px; font-weight: 600; color: var(--white); text-decoration: none; letter-spacing: 0.2px; }
  .main-nav .nav-contact { background: var(--orange); padding: 9px 9px; border-radius: 1px; margin-left: -6px; }

  .hero-copy { position: absolute; left: 0; top: 143px; width: 720px; text-align: center; color: var(--white); }
  .hero-title { font-size: 29px; font-weight: 800; line-height: 30px; letter-spacing: 0.3px; }
  .hero-kicker { margin-top: 9px; font-size: 17px; font-weight: 600; letter-spacing: 0.5px; }
  .hero-lede { margin: 8px auto 0; width: 380px; font-size: 12px; font-weight: 600; line-height: 17px; }
  .hero-actions { margin-top: 15px; display: flex; justify-content: center; gap: 17px; }

  .btn { display: inline-flex; align-items: center; justify-content: center; height: 30px; color: var(--white); font-size: 9px; font-weight: 700; letter-spacing: 0.4px; text-decoration: none; border-radius: 1px; }
  .btn-blue { background: var(--sky-blue); width: 131px; }
  .btn-orange { background: var(--orange); width: 131px; }
  .btn-small { width: 79px; }

  .about { position: absolute; left: 0; top: 432px; width: 720px; height: 315px; }
  .about-photo {
    position: absolute; left: 45px; top: 38px; width: 307px; height: 233px; border-radius: 50% 40% 50% 50%;
    background: radial-gradient(circle at 45% 45%, #d6b08a 0%, #9b7555 45%, #3a3230 100%);
  }
  .about-text { position: absolute; left: 370px; top: 37px; width: 303px; font-size: 9.4px; line-height: 15px; }
  .about-text p + p { margin-top: 6px; }
  .about-text .highlight { color: var(--orange); font-weight: 700; }
  .about-text .btn { margin-top: 15px; }

  .affiliates { position: absolute; left: 0; top: 747px; width: 720px; height: 153px; background: var(--light-band); }
  .affiliates-title { position: absolute; top: 32px; width: 720px; text-align: center; color: var(--navy); font-size: 11px; font-weight: 700; letter-spacing: 0.3px; }
  .affiliate-badges { position: absolute; top: 63px; left: 0; width: 720px; display: flex; justify-content: center; align-items: center; gap: 30px; }
  .badge-tkr { width: 50px; height: 50px; background: #6aad3d; border-radius: 3px; }
  .badge-funds { width: 170px; height: 36px; background: #d9ecd6; border-radius: 4px; }
  .badge-bnf { width: 58px; height: 50px; background: #0e2a5c; }
  .badge-settle { width: 139px; height: 36px; background: #e3d4ea; border-radius: 4px; }

  .service-card { position: absolute; top: 921px; width: 307px; height: 145px; color: var(--white); }
  .card-landlords { left: 45px; background: var(--sky-blue); }
  .card-tenants { left: 369px; background: var(--navy); }
  .card-art { position: absolute; left: 17px; top: 29px; width: 78px; height: 86px; border-radius: 50%; background: rgba(255,255,255,0.22); }
  .card-body { position: absolute; left: 115px; top: 14px; width: 176px; }
  .card-title { font-size: 14px; font-weight: 700; letter-spacing: 0.3px; }
  .card-text { margin-top: 5px; font-size: 9.4px; line-height: 13px; }
  .card-body .btn { margin-top: 9px; }

  .site-footer { position: absolute; left: 0; top: 1090px; width: 720px; height: 110px; background: var(--footer); color: var(--white); }
  .footer-nav { position: absolute; left: 44px; top: 32px; display: flex; gap: 25px; }
  .footer-nav a { color: var(--white); font-size: 8px; font-weight: 700; text-decoration: none; }
  .copyright { position: absolute; left: 45px; top: 57px; font-size: 7.5px; line-height: 14px; color: #bdbdbd; }
  .footer-brand { left: 306px; top: 44px; width: 120px; }
  .follow { position: absolute; left: 575px; top: 33px; width: 101px; }
  .follow-title { font-size: 8px; font-weight: 700; }
  .social-links { margin-top: 11px; display: flex; justify-content: space-between; }
  .social-links a { color: var(--white); font-size: 7px; font-weight: 600; text-decoration: none; }
</style>
</head>
<body>

<section class="hero">
  <div class="hero-photo" role="img" aria-label="Coastal photograph of a modern house on a green cliff above the ocean with mountains behind"></div>
  <svg class="hero-cut" viewBox="0 0 720 58" preserveAspectRatio="none" aria-hidden="true">
    <polygon points="0,0 360,58 720,0 720,58 0,58" fill="#ffffff"/>
  </svg>

  <div class="brand header-brand">
    <span class="brand-dot"></span>
    <span class="brand-name">HARBOUR VALE LETTINGS</span>
  </div>

  <nav class="main-nav">
    <a href="#">HOME</a>
    <a href="#">LANDLORDS</a>
    <a href="#">TENANTS</a>
    <a href="#" class="nav-contact">CONTACT US</a>
  </nav>

  <div class="hero-copy">
    <h1 class="hero-title">WELCOME TO<br>HARBOUR VALE LETTINGS</h1>
    <p class="hero-kicker">PROPERTY MANAGEMENT</p>
    <p class="hero-lede">Harbour Vale Lettings has emerged after over 20 years of privately managing our own rental.</p>
    <div class="hero-actions">
      <a href="#" class="btn btn-blue">LANDLORD ENQUIRY</a>
      <a href="#" class="btn btn-orange">TENANTS ENQUIRY</a>
    </div>
  </div>
</section>

<section class="about">
  <div class="about-photo" role="img" aria-label="Photograph of a handshake over a desk with a model house, documents and keys"></div>
  <div class="about-text">
    <p><span class="highlight">Harbour Vale Lettings</span> has emerged after over 20 years of privately managing our own rental properties. We are family run and decided to move all of our properties under one ‘umbrella’. Now professionally set up as a legal entity, Harbour Vale is looking to welcome new tenants and landlords to an innovative and fresh way of letting property.</p>
    <p>We always maintain a high standard of service and our friendly and helpful team are experienced in all areas and offer an excellent service in helping landlords and tenants deal with problems and issues they face daily.</p>
    <p>Out of hours emergency service which means we are there<br>(in an emergency) for our tenants and landlords 24/7.</p>
    <a href="#" class="btn btn-blue">LANDLORD ENQUIRY</a>
  </div>
</section>

<section class="affiliates">
  <h2 class="affiliates-title">WE ARE MEMBERS OF OR AFFILIATED TO</h2>
  <div class="affiliate-badges">
    <div class="badge-tkr" role="img" aria-label="TKR membership badge"></div>
    <div class="badge-funds" role="img" aria-label="Funds Guard Scheme membership badge"></div>
    <div class="badge-bnf" role="img" aria-label="BNF registration badge"></div>
    <div class="badge-settle" role="img" aria-label="Tenancy Settle Scheme membership badge"></div>
  </div>
</section>

<article class="service-card card-landlords">
  <div class="card-art" role="img" aria-label="Illustration of a landlord with a house"></div>
  <div class="card-body">
    <h3 class="card-title">LANDLORDS</h3>
    <p class="card-text">Whether you are an experienced andlord with a large portfolio or looking to take your first steps into the buy to let market,</p>
    <a href="#" class="btn btn-orange btn-small">READ MORE</a>
  </div>
</article>

<article class="service-card card-tenants">
  <div class="card-art" role="img" aria-label="Illustration of a tenant with a house and key"></div>
  <div class="card-body">
    <h3 class="card-title">TENANTS</h3>
    <p class="card-text">Start your renting journey with Harbour Vale Lettings for a seamless renting experience and complete peace of mind.</p>
    <a href="#" class="btn btn-orange btn-small">READ MORE</a>
  </div>
</article>

<footer class="site-footer">
  <nav class="footer-nav">
    <a href="#">HOME</a>
    <a href="#">LANDLORDS</a>
    <a href="#">TENANTS</a>
  </nav>
  <p class="copyright">Copyright © 2025 Company Name.<br>All rights reserved.</p>

  <div class="brand footer-brand">
    <span class="brand-dot"></span>
    <span class="brand-name">HARBOUR VALE LETTINGS</span>
  </div>

  <div class="follow">
    <p class="follow-title">FOLLOW US</p>
    <div class="social-links">
      <a href="#">Kin</a>
      <a href="#">Chirp</a>
      <a href="#">Lens</a>
      <a href="#">Guild</a>
      <a href="#">Clip</a>
    </div>
  </div>
</footer>

</body>
</html>
```